Yard Sign Design for Roofing Contractor

We are looking for a new design for our yard signs used on all jobs we build. We are looking for a way to brand the company and are hoping that this contest can give us a "theme" we can incorporate into out other marketing items such as, vehicle graphics, apparel, etc... I have attached a copy of our logo to be used on the sign, it can be "shadowed" with a color to enhance the look and the sign, but please keep the basic logo design. Attached are some samples of construction colors the boss was thinking of along with a picture of our current yard sign to help give some direction and let you know what info is needed on the sign.The darker construction yellow may work better than the fluorescent yellow, but won't know without visual aid. We are not tied to any particular color as of now, so they do have freedom of design as long as keeping with the construction feel. (Just another thought, potentially a reflective construction tape look would be interesting so signs are visable at night)
Updates

Reason: Meeting with new web designers next week to discuss best option to incorporate into our website.Thank you for the submissions!

Target Market(s)

Want signs to stand out when driving by and visibility in neighborhood where sign is posted for potential referrals

Industry/Entity Type

Contractor

Colors
fbed22
fece3e
f37122

Requirements
Must have
• Information that is on our current signs, image attached. I uploaded a .pdf file showing some options that could work for adding "shading" to our logo if you choose to do so.
• Sign should measure 18" T, 24" W
Nice to have
• Interested is seeing designs using construction tape look, images attached

```html
<!DOCTYPE html>
<html lang="en">
<head>
<meta charset="utf-8">
<title>Harlow Construction – Yard Sign</title>
<link rel="stylesheet" href="https://fonts.googleapis.com/css2?family=Tinos:wght@400;700&family=Open+Sans:wght@700&family=Oswald:wght@700&display=swap">
<style>
  :root {
    --hazard-yellow: #fece3e;
    --hazard-black: #141414;
    --ink: #0d0d0d;
    --accent: #f2c200;
    --frame-white: #f4f4f4;
    --plate-light: #f7f7f7;
    --plate-mid: #d9d9d9;
    --plate-dark: #b5b5b5;
    --seal-gold: #f2c230;
    --seal-brown: #6b4a10;
    --ribbon-red: #d41616;
    --badge-grey: #7a7a7a;
  }
  html, body {
    margin: 0;
    padding: 0;
    width: 1200px;
    height: 943px;
    overflow: hidden;
    background: #ffffff;
  }
  .yard-sign {
    position: relative;
    width: 1200px;
    height: 943px;
    overflow: hidden;
    background: repeating-linear-gradient(
      -45deg,
      var(--hazard-black) 0 70px,
      var(--hazard-yellow) 70px 140px
    );
  }
  .inner-frame {
    position: absolute;
    left: 38px; top: 36px; right: 38px; bottom: 36px;
    border: 5px solid var(--frame-white);
  }
  .metal-plate {
    position: absolute;
    left: 130px; top: 150px;
    width: 950px; height: 610px;
    border-radius: 22px;
    background: linear-gradient(160deg, var(--plate-light) 0%, var(--plate-mid) 45%, var(--plate-light) 70%, var(--plate-dark) 100%);
    box-shadow: 6px 8px 0 var(--plate-dark), 0 10px 22px rgba(0,0,0,.45);
    transform: rotate(-2deg);
  }
  .phone-plate {
    position: absolute;
    left: 212px; top: 700px;
    width: 782px; height: 176px;
    border-radius: 14px;
    background: linear-gradient(170deg, var(--plate-light) 0%, var(--plate-mid) 55%, var(--plate-light) 80%, var(--plate-dark) 100%);
    box-shadow: 4px 6px 0 var(--plate-dark), 0 10px 20px rgba(0,0,0,.45);
    transform: rotate(-3deg);
  }
  .screw {
    position: absolute;
    width: 44px; height: 44px;
    border-radius: 50%;
    background: radial-gradient(circle at 35% 35%, #ffffff, #b8b8b8 70%, #8c8c8c);
    box-shadow: inset 0 0 0 2px #c8c8c8;
  }
  .phone-plate .screw {
    width: 34px; height: 34px;
  }
  .award-seal {
    position: absolute;
    left: 252px; top: 80px;
    width: 130px; height: 160px;
  }
  .award-seal .seal-text {
    position: absolute;
    left: 0; top: 26px; width: 130px;
    text-align: center;
    font-family: "Open Sans", sans-serif;
    font-weight: 700;
    font-size: 15px;
    line-height: 17px;
    color: var(--seal-brown);
  }
  .accreditation-badge {
    position: absolute;
    left: 858px; top: 138px;
    width: 68px; height: 112px;
    border-radius: 6px;
    background: #efefef;
    border: 2px solid var(--badge-grey);
  }
  .website {
    position: absolute;
    left: 0; top: 270px; width: 1200px;
    text-align: center;
    font-family: "Open Sans", sans-serif;
    font-weight: 700;
    font-size: 38px;
    line-height: 52px;
    color: var(--ink);
    white-space: nowrap;
  }
  .company-name {
    position: absolute;
    left: 260px; top: 338px;
    width: 680px; height: 250px;
    margin: 0;
    border: 4px solid var(--ink);
    box-sizing: border-box;
    text-align: center;
    font-family: "Tinos", serif;
    font-weight: 700;
    color: var(--ink);
    white-space: nowrap;
    overflow: hidden;
  }
  .company-name .name-main {
    display: block;
    font-size: 128px;
    line-height: 138px;
    margin-top: 10px;
  }
  .company-name .name-sub {
    display: block;
    font-size: 70px;
    line-height: 80px;
  }
  .services {
    position: absolute;
    left: 0; top: 612px; width: 1200px;
    display: flex;
    justify-content: center;
    align-items: center;
    gap: 26px;
    font-family: "Tinos", serif;
    font-size: 46px;
    line-height: 56px;
    color: var(--ink);
  }
  .services .dot {
    width: 32px; height: 32px;
    border-radius: 50%;
    background: radial-gradient(circle at 35% 35%, #ffffff, #9a9a9a 75%, #6e6e6e);
  }
  .phone {
    position: absolute;
    left: 212px; top: 700px;
    width: 782px; height: 176px;
    padding: 0 72px;
    box-sizing: border-box;
    display: flex;
    align-items: center;
    justify-content: center;
    font-family: "Oswald", sans-serif;
    font-weight: 700;
    font-size: 104px;
    line-height: 1;
    white-space: nowrap;
    color: var(--ink);
    text-shadow: 3px 3px 0 var(--accent);
    transform: rotate(-3deg) skewX(-6deg);
  }
</style>
</head>
<body>
<main class="yard-sign">
  <div class="inner-frame"></div>

  <div class="metal-plate">
    <span class="screw" style="left:40px; top:50px;"></span>
    <span class="screw" style="right:40px; top:30px;"></span>
  </div>

  <div class="award-seal">
    <svg width="130" height="160" viewBox="0 0 130 160" aria-hidden="true">
      <polygon points="30,90 50,95 38,150 26,128 6,138" fill="var(--ribbon-red)"/>
      <polygon points="100,90 80,95 92,150 104,128 124,138" fill="var(--ribbon-red)"/>
      <circle cx="65" cy="62" r="60" fill="var(--seal-gold)"/>
      <circle cx="65" cy="62" r="50" fill="none" stroke="#fff3b0" stroke-width="2"/>
    </svg>
    <div class="seal-text">AWARD<br>WINNING!</div>
  </div>

  <div class="accreditation-badge"></div>

  <div class="phone-plate">
    <span class="screw" style="left:18px; top:71px;"></span>
    <span class="screw" style="right:18px; top:30px;"></span>
  </div>

  <div class="website">www.harlowroofing.com</div>

  <h1 class="company-name">
    <span class="name-main">HARLOW</span>
    <span class="name-sub">CONSTRUCTION</span>
  </h1>

  <div class="services">
    <span>ROOF</span><span class="dot"></span>
    <span>SIDING</span><span class="dot"></span>
    <span>GUTTERS</span>
  </div>

  <div class="phone">405-555-0142</div>
</main>
</body>
</html>
```